Diesel Trailer Manufacturer Website Design

We are working with a Trailer Manufacturer in Texas. They provide custom-made trailers for diesel trucks throughout the US.
Some sites to use for content/competitors:
www.birchhaulers.com
https://velmotrailers.com
http://www.dunhollowcustomtrailers.com/
https://www.pellingtrailer.com
https://www.roadwren.com
Thank you for taking the time to consider designing a website for us. We are web developers based in Stockton, CA, USA. Most of our projects go through the same process. Understanding this process may help you win a project with us. We custom-code all of our websites in-house. We don’t have any requirements as to what tools you use for your design, but we ask that you follow these guidelines.
IMAGES:
If you use any images or icons in the design, we ask that you have a link to the asset so we can purchase the image/icon. Most of the designs we submit do not have the customer’s images on them unless they have some great images. Be creative; show us the feeling you are trying to portray with your image choices. Use any royalty-free site you choose. We subscribe to Quillor and mainly use their images, but we can purchase images outside of Quillor. PLEASE NOTE: we will not submit designs to clients with watermarks on the images.
FONTS:
We ask that you identify the fonts you’re using in the design. This can be done in a message if you want. We typically use Fennix Fonts and Quillor Fonts.
CONTENT:
We're always open to different content and ideas. We often submit designs with stock images so the client can see our vision. We typically take pictures after the website launch to use their images with our vision. Lorem Ipsum is fine for paragraphs, but we ask that you make the Headers with correct English. We want to be able to show the vision and identify the sections of the website.
INSPIRATION:
We typically add a couple of links in the brief of websites we like to help you get started in your design.
REVISIONS:
We do not often ask for revisions of the designs unless we see something in the design that may not appeal to the client. If there are slight changes that we want to make, we do that in the development process.
FEEDBACK:
We rarely give feedback on designs during the design process. We are working on many website projects and do not have the time to provide feedback. We usually respond if your request is well thought out and asks specific questions, but a note asking “feedback, please” usually goes unanswered.
1 page

```html
<!DOCTYPE html>
<html lang="en">
<head>
<meta charset="utf-8">
<title>Brasscoil – Diesel Trailer Manufacturer</title>
<link href="https://fonts.googleapis.com/css2?family=Cinzel:wght@600;700&family=Nunito+Sans:ital,wght@0,400;0,600;0,700;1,400&display=swap" rel="stylesheet">
<style>
:root{
  --red:#9b1406;
  --red-deep:#7e0f04;
  --ink:#1c1c1c;
  --text:#4a4a4a;
  --dark:#262626;
  --white:#ffffff;
}
*{margin:0;padding:0;box-sizing:border-box}
html,body{width:1200px;height:3481px;overflow:hidden;background:var(--white)}
body{font-family:"Nunito Sans",sans-serif;color:var(--text);position:relative}
.abs{position:absolute}
.btn{position:absolute;left:511px;width:178px;height:61px;border-radius:31px;background:var(--red);color:var(--white);font:600 17px "Nunito Sans",sans-serif;display:flex;align-items:center;justify-content:center;letter-spacing:.2px}
.divider{position:absolute;left:533px;width:134px;height:14px}
.section-title{position:absolute;left:0;width:1200px;text-align:center;font-family:"Cinzel",serif;font-weight:700;line-height:1;text-transform:uppercase}

/* header */
.site-header{position:absolute;top:0;left:0;width:1200px;height:119px;background:var(--white)}
.brand{position:absolute;left:145px;top:30px;display:flex;align-items:center;gap:10px;font-family:"Cinzel",serif;font-weight:700;font-size:30px;color:var(--red);text-transform:uppercase}
.brand-dot{width:16px;height:16px;border-radius:50%;background:var(--red)}
.call-badge{position:absolute;left:676px;top:0;width:378px;height:45px}
.call-text{position:absolute;left:730px;top:0;height:45px;display:flex;align-items:center;gap:10px;color:var(--white);font:700 20px "Nunito Sans",sans-serif}
.main-nav{position:absolute;top:78px;left:467px;display:flex;gap:26px;font:600 14px "Nunito Sans",sans-serif;color:var(--ink)}

/* hero */
.hero{position:absolute;top:119px;left:0;width:1200px;height:570px;background:linear-gradient(180deg,#2c4e80 0%,#6d87a8 35%,#a6a9a6 60%,#7b7258 85%,#5a5040 100%)}
.hero-title{top:250px;font-size:59px;color:var(--white);line-height:68px}
.dots{position:absolute;left:1131px;top:365px;display:flex;flex-direction:column;gap:12px}
.dots span{width:8px;height:8px;border-radius:50%;background:var(--white)}
.dots span.on{background:var(--red)}

/* welcome */
.welcome-bg{position:absolute;top:620px;left:0;width:1200px;height:700px;background:linear-gradient(180deg,#ffffff 0%,#f1f3f6 50%,#e6e9ee 100%)}
.welcome-text{position:absolute;left:216px;top:843px;width:768px;text-align:center;font-size:16px;line-height:29px;color:#555}

/* why */
.why-text{position:absolute;left:310px;top:1430px;width:580px;text-align:center;font-size:15.5px;line-height:29px;color:var(--white)}

/* trailers */
.trailer-grid{position:absolute;left:145px;top:1944px;display:grid;grid-template-columns:300px 300px 300px;grid-template-rows:322px 322px;gap:5px}
.trailer-tile{position:relative}
.trailer-tile.featured{outline:5px solid var(--red);outline-offset:-5px}
.tile-label{position:absolute;left:50px;bottom:5px;width:196px;height:44px;background:var(--red);color:var(--white);font:700 20px "Nunito Sans",sans-serif;display:flex;align-items:center;justify-content:center}

/* testimonials */
.quote{position:absolute;left:250px;top:3044px;width:700px;text-align:center;font-style:italic;font-size:17px;line-height:27px;color:var(--white)}
.quote-author{position:absolute;left:0;width:1200px;top:3145px;text-align:center;font:700 17px "Nunito Sans",sans-serif;color:var(--white)}
.quote-arrows{position:absolute;left:570px;top:3200px;display:flex;gap:6px}

/* footer */
.site-footer{position:absolute;left:0;top:3297px;width:1200px;height:184px;background:var(--dark)}
.footer-brand{position:absolute;left:162px;top:60px;display:flex;align-items:center;gap:10px;font-family:"Cinzel",serif;font-weight:700;font-size:32px;color:var(--white);text-transform:uppercase}
.social{position:absolute;left:449px;top:37px;display:flex;gap:6px}
.social span{width:21px;height:21px;border-radius:50%;background:var(--white)}
.footer-nav{position:absolute;left:446px;top:83px;display:flex;gap:26px;font:700 14px "Nunito Sans",sans-serif;color:var(--white)}
.legal{position:absolute;left:446px;top:122px;font-size:12px;color:#d8d8d8}
</style>
</head>
<body>

<header class="site-header">
  <div class="brand"><span class="brand-dot"></span>Brasscoil</div>
  <svg class="call-badge" viewBox="0 0 378 45"><polygon points="0,0 378,0 340,45 36,45" fill="var(--red)"/></svg>
  <div class="call-text">
    <svg width="30" height="30" viewBox="0 0 30 30"><circle cx="15" cy="15" r="14" fill="#fff"/><path d="M10 8c1-1 2 0 3 2s0 2-1 3c1 2 3 4 5 5 1-1 1-2 3-1s3 2 2 3c-1 2-3 3-6 1-3-2-6-5-7-8-1-2 0-4 1-5z" fill="var(--red)"/></svg>
    CALL : +1 555 014 2270
  </div>
  <nav class="main-nav"><span>HOME</span><span>OUR TRAILERS</span><span>PARTS &amp; SERVICE</span><span>FINANCING</span><span>CAREERS</span><span>CONTACT</span></nav>
</header>

<section class="hero" role="img" aria-label="Photo of a polished steel diesel tanker trailer on a road under a cloudy blue sky"></section>
<div class="welcome-bg" role="img" aria-label="Faded photo of a refinery with tanker trucks"></div>
<svg class="abs" style="left:0;top:600px" width="1200" height="90" viewBox="0 0 1200 90">
  <polygon points="0,86 600,14 1200,76 1200,90 0,90" fill="#fff"/>
  <path d="M531 15 A69 69 0 0 0 669 15 Z" fill="var(--red)"/>
  <polyline points="585,31 600,44 615,31" fill="none" stroke="#fff" stroke-width="4"/>
</svg>
<h1 class="section-title hero-title">Diesel Trailer<br>Manufacturer</h1>
<div class="btn" style="top:412px">GET STARTED</div>
<div class="dots"><span></span><span></span><span class="on"></span></div>

<h2 class="section-title" style="top:736px;font-size:54px;color:var(--ink)">Welcome</h2>
<svg class="divider" style="top:801px" viewBox="0 0 134 14"><path d="M0 5 H55 Q67 5 67 12 Q67 5 79 5 H134" fill="none" stroke="#222" stroke-width="2"/></svg>
<p class="welcome-text">Sed ut perspiciatis unde omnis iste natus error sit voluptatem accusantium doloremque laudantium, totam rem aperiam, eaque ipsa quae ab illo inventore veritatis et quasi architecto beatae vitae dicta sunt explicabo. Nemo enim ipsam voluptatem quia voluptas sit aspernatur aut odit aut fugit, sed quia consequuntur magni dolores eos qui ratione voluptatem sequi nesciunt. Neque porro quisquam est, qui dolorem ipsum quia dolor sit amet, consectetur, adipisci velit, sed quia non numquam eius modi tempora incidunt</p>
<div class="btn" style="top:1024px">READ MORE</div>

<svg class="abs" style="left:0;top:1150px" width="1200" height="560" viewBox="0 0 1200 560" role="img" aria-label="Dark photo of a semi truck cab beside a trailer on a highway">
  <defs><linearGradient id="whyPhoto" x1="0" y1="0" x2="1" y2="1"><stop offset="0" stop-color="#3a3d45"/><stop offset=".6" stop-color="#2a2c33"/><stop offset="1" stop-color="#4a4a4e"/></linearGradient></defs>
  <polygon points="412,1 1200,167 1200,559 7,559" fill="url(#whyPhoto)"/>
  <polygon points="0,173 408,0 0,559" fill="var(--red)"/>
  <line x1="410" y1="0" x2="4" y2="559" stroke="#fff" stroke-width="6"/>
</svg>
<h2 class="section-title" style="top:1321px;font-size:54px;color:var(--white)">Why Us?</h2>
<svg class="divider" style="top:1387px" viewBox="0 0 134 14"><path d="M0 5 H55 Q67 5 67 12 Q67 5 79 5 H134" fill="none" stroke="#fff" stroke-width="2"/></svg>
<p class="why-text">Sed ut perspiciatis unde omnis iste natus error sit voluptatem accusantium doloremque laudantium, totam rem aperiam, eaque ipsa quae ab illo inventore veritatis et quasi architecto beatae vitae dicta sunt explicabo.</p>
<div class="btn" style="top:1547px">READ MORE</div>

<h2 class="section-title" style="top:1813px;font-size:56px;color:var(--ink)">Our <span style="color:var(--red)">Trailers</span></h2>
<svg class="divider" style="top:1884px" viewBox="0 0 134 14"><path d="M0 5 H55 Q67 5 67 12 Q67 5 79 5 H134" fill="none" stroke="#222" stroke-width="2"/></svg>
<div class="trailer-grid">
  <div class="trailer-tile" role="img" aria-label="Photo of a blue truck cab front" style="background:linear-gradient(135deg,#b7a25a,#2f4fa8 55%,#8c8f92)"></div>
  <div class="trailer-tile featured" role="img" aria-label="Photo of a chrome tanker trailer on a road" style="background:linear-gradient(180deg,#3d4a35,#7d8478 55%,#5e5a55)"><div class="tile-label">HEAVY HAUL</div></div>
  <div class="trailer-tile" role="img" aria-label="Photo of a tanker trailer at an industrial plant at sunset" style="background:linear-gradient(180deg,#4a5366,#a49f9a 55%,#6e6e70)"></div>
  <div class="trailer-tile" role="img" aria-label="Photo of a red and silver tanker trailer on a road at dusk" style="background:linear-gradient(135deg,#d9a860,#9a3b2a 55%,#3d3c3e)"></div>
  <div class="trailer-tile" role="img" aria-label="Photo of a yellow tanker truck on a dirt field" style="background:linear-gradient(180deg,#8fb2cf,#c57a35 50%,#6b6548)"></div>
  <div class="trailer-tile" role="img" aria-label="Photo of a red truck pulling a steel tanker" style="background:linear-gradient(135deg,#486b32,#d42a24 50%,#9a9a9c)"></div>
</div>
<div class="btn" style="top:2636px">LOAD MORE</div>

<svg class="abs" style="left:0;top:2735px" width="1200" height="563" viewBox="0 0 1200 563" role="img" aria-label="Red-tinted photo of trucks with a grey photo of a truck fleet at the right">
  <defs><linearGradient id="fleet" x1="0" y1="0" x2="1" y2="1"><stop offset="0" stop-color="#c9c9cc"/><stop offset="1" stop-color="#8d8e92"/></linearGradient></defs>
  <polygon points="798,0 1200,168 1200,540" fill="url(#fleet)"/>
  <polygon points="0,176 788,0 1200,562 0,562" fill="var(--red)"/>
  <line x1="792" y1="0" x2="1200" y2="556" stroke="#fff" stroke-width="6"/>
</svg>
<h2 class="section-title" style="top:2918px;font-size:56px;color:var(--white)">Testimonials</h2>
<svg class="divider" style="top:2986px" viewBox="0 0 134 14"><path d="M0 5 H55 Q67 5 67 12 Q67 5 79 5 H134" fill="none" stroke="#fff" stroke-width="2"/></svg>
<p class="quote">“Sed ut perspiciatis unde omnis iste natus error sit voluptatem accusantium doloremque laudantium, totam rem aperiam, eaque ipsa quae ab illo inventore veritatis et quasi architecto beatae vitaexplicabm quiuntur magni dolores eos qui ratione”</p>
<p class="quote-author">- JOHN DOE,CUSTOMER</p>
<div class="quote-arrows">
  <svg width="28" height="28" viewBox="0 0 28 28"><circle cx="14" cy="14" r="12.5" fill="none" stroke="#fff" stroke-width="2"/><path d="M20 14H8M13 9l-5 5 5 5" fill="none" stroke="#fff" stroke-width="2"/></svg>
  <svg width="28" height="28" viewBox="0 0 28 28"><circle cx="14" cy="14" r="12.5" fill="none" stroke="#fff" stroke-width="2"/><path d="M8 14h12M15 9l5 5-5 5" fill="none" stroke="#fff" stroke-width="2"/></svg>
</div>

<footer class="site-footer">
  <div class="footer-brand"><span class="brand-dot"></span>Brasscoil</div>
  <div class="social"><span></span><span></span><span></span><span></span></div>
  <nav class="footer-nav"><span>HOME</span><span>OUR TRAILERS</span><span>PARTS &amp; SERVICE</span><span>FINANCING</span><span>CAREERS</span><span>CONTACT</span></nav>
  <p class="legal">© 2023 Brasscoil. All Rights Reserved &nbsp;|&nbsp; Privacy Policy &nbsp;|&nbsp; Terms</p>
</footer>

</body>
</html>
```